Homepage for experience sharing site- interesting, fun and personable!

We need a homepage design for an experience sharing website. The tag line is 'find, promote and share great times!' The homepage should be exciting and innovative and illustrate the values of the site: possibility, freedom and life. It should be fun and personable.

To give you a clearer example, here are a few of the 'great times' users will be sharing on the site:

Club night, warehouse rave or beach gig
Antarctic expedition, Cambodian jungle trek
Cooking and surfing classes
Sumo speed dating
Drag racing and quad biking
Birthday parties, pub crawls and comedy nights

We like the idea of some sort of map or background image from which a few experiences pop up; however we are open to other ideas. The links below should give you an idea of the concept.

http://www.korvane.com/harbor#/harbor-story
http://www.pimbleo.com/map/
http://www.vidquarra.com/watch?v=QT7KWLR2zpa
Updates

Hi,

please do not feel that your design must include a map, that was just an idea. If you can produce a design that delivers the message immediately and gets the user interested without a map then that is great! 

Please do not feel constrained.

Thanks,

Marisol

Hi,

I've created and attached two examples to the brief, which I hope will provide some guidance. I want the homepage design to concentrate on the human element and the concept of creating and sharing experiences.

Thanks,

Marisol  

Target Market(s)

18-37 age range. People who enjoy life and new experiences.

Industry/Entity Type

Racing

Requirements
Must have
• It must communicate the human element of the site... please see the attached examples I made as guidance

It must deliver the message as simply as possible

Could you ensure that your design includes the following elements please:

* breadcrumbs
* a search box
* the login and register should be part of the header block
Should not have
• Unnecessary elements

Only yellow

```html
<!DOCTYPE html>
<html lang="en">
<head>
<meta charset="utf-8">
<title>DAYWELLSPENT.COM – Home</title>
<link href="https://fonts.googleapis.com/css2?family=Varela+Round&family=Stardos+Stencil:wght@700&display=swap" rel="stylesheet">
<style>
:root{
  --ink-dark:#3a3a3a;
  --band:#5d5a4b;
  --yellow:#ffff00;
  --pale-yellow:#fff8c4;
  --blue:#0000cc;
  --navy:#000080;
  --red:#ee1111;
  --panel-grey:#c9c9c9;
  --strip-grey:#b8b8b8;
  --white:#ffffff;
  --text:#111111;
  --footer:#777777;
  --sky:linear-gradient(160deg,#2a5fb0 0%,#5e93d8 45%,#d8c9a0 75%,#e9dcb8 100%);
}
*{box-sizing:border-box;margin:0;padding:0}
html,body{width:884px;height:1200px;overflow:hidden;background:var(--white)}
body{font-family:"Varela Round",sans-serif;color:var(--text)}
.page{position:relative;width:1008px;height:1368px;transform:scale(.87698);transform-origin:0 0;background:var(--white)}
.abs{position:absolute}
a{color:inherit;text-decoration:none}

/* header */
.topbar{left:0;top:0;width:1008px;height:72px;background:var(--ink-dark);border-bottom:4px solid var(--yellow)}
.brand{left:18px;top:35px;display:flex;align-items:center;gap:7px;color:var(--white);font-size:17px;line-height:24px;letter-spacing:.2px}
.brand-mark{width:14px;height:14px;background:var(--yellow);flex:none}
.nav{left:222px;top:38px;display:flex;align-items:center;font-size:14px;color:var(--white)}
.nav a{padding:0 17px;line-height:32px;letter-spacing:.4px}
.nav .current{background:var(--yellow);color:var(--blue);border-radius:4px 4px 0 0;padding:0 9px;font-size:16px}
.nav .caret{font-size:9px;margin-left:2px}
.account{left:842px;top:43px;width:134px;height:21px;background:var(--white);color:var(--blue);font-size:14px;line-height:21px;text-align:center;letter-spacing:.3px}
.subband{left:0;top:76px;width:1008px;height:47px;background:var(--band);border-bottom:2px solid #2c2b25}
.tagline{left:20px;top:86px;font-family:"Stardos Stencil",serif;font-size:24px;color:#f1ecd8;letter-spacing:.5px}
.search-field{left:696px;top:88px;width:178px;height:23px;background:var(--white);border-radius:12px;border:1px solid #999}
.search-btn{left:888px;top:86px;width:92px;height:27px;background:var(--blue);color:var(--white);border:1px solid #cfd;font-size:16px;line-height:25px;text-align:center;letter-spacing:.6px}

/* dropdown */
.dropdown{left:301px;top:77px;width:281px;height:190px;background:rgba(255,250,200,.88);border:1px solid #e6dc59;z-index:5;padding-top:11px}
.dropdown li{list-style:none;color:var(--red);font-size:15px;line-height:22px;padding-left:7px;letter-spacing:.6px}
.dropdown li.active{background:var(--yellow)}

/* feature */
.feature{left:20px;top:138px;width:962px;height:307px;background:var(--ink-dark);border:1px solid #222}
.photo{background:linear-gradient(135deg,#cfc8bd,#8d8478 60%,#b9a68a)}
.thumb{width:52px;height:42px;background:var(--sky);border:2px solid #ddd}
.story-card{left:432px;top:198px;width:535px;height:190px;background:var(--white);border-radius:6px;padding:14px 20px 0 19px}
.story-card h3{font-weight:normal;font-size:14px;color:#bbb;margin-left:20px}
.story-card p{font-size:13px;line-height:19px;letter-spacing:.3px;margin-top:4px}
.btn-more{background:var(--blue);color:var(--white);font-size:13px;line-height:23px;text-align:center;letter-spacing:.6px;border:1px solid #ccf}
.meta{font-size:11px;color:#999;letter-spacing:1px}
.share{left:850px;top:398px;width:113px;height:42px;background:var(--white);border-radius:6px;display:flex;gap:5px;align-items:center;justify-content:center}
.share span{width:28px;height:28px;background:#2a6cc8;border-radius:6px;border:1px solid #144}

/* carousel */
.strip{left:55px;top:469px;width:887px;height:75px;background:var(--strip-grey);border:1px solid #666;border-radius:6px}
.strip-thumb{top:476px;width:80px;height:61px;background:var(--sky);border:2px solid #333}
.strip-focus{left:270px;top:445px;width:149px;height:119px;background:var(--ink-dark)}
.arrow{top:478px;color:var(--blue);font-size:58px;line-height:58px;font-weight:bold;transform:scaleX(.6)}

/* left column */
.list-head{left:18px;top:600px;width:341px;height:48px;background:#e2e2ee;border:1px solid var(--blue);display:flex;align-items:center;padding-left:16px;gap:8px;color:var(--blue);font-size:15px;letter-spacing:.6px}
.qmark{width:32px;height:32px;border-radius:8px;background:#d4d4d4;color:var(--white);font-size:22px;line-height:32px;text-align:center;flex:none}
.list-body{left:18px;top:647px;width:341px;height:638px;border-right:1px solid var(--blue)}
.item{position:absolute;left:12px;width:315px;height:72px;padding:10px 18px 0 4px;display:flex;gap:6px;border-radius:5px}
.item.hover{background:#eaeaea}
.item .qmark{width:30px;height:30px;line-height:30px}
.item h4{font-weight:normal;color:var(--blue);font-size:14px;line-height:14px}
.item p{font-size:11px;line-height:12px;letter-spacing:.2px}
.item .by{display:flex;justify-content:space-between;font-size:10px;line-height:14px;letter-spacing:.4px}
.rule-blue{height:2px;background:var(--blue)}
.pager{font-size:12px;color:var(--blue);letter-spacing:.8px}

/* right column */
.right{left:358px;top:600px;width:622px;height:675px;background:var(--panel-grey);border:1px solid var(--blue)}
.read-panel{left:368px;top:613px;width:604px;height:340px;background:var(--white);border-radius:6px 6px 0 0}
.read-panel h3{position:absolute;left:223px;top:13px;font-weight:normal;color:var(--blue);font-size:14px;letter-spacing:.6px}
.read-panel .body{position:absolute;left:223px;top:34px;width:368px;font-size:13px;line-height:14px;letter-spacing:.6px;text-align:justify}
.read-panel .body p{text-indent:36px;margin-bottom:14px}
.tab{top:927px;height:26px;background:var(--yellow);border:1px solid var(--blue);border-bottom:none;border-radius:6px 6px 0 0;color:var(--blue);font-size:15px;line-height:26px;padding:0 6px;letter-spacing:.6px}
.grid-panel{left:368px;top:952px;width:604px;height:313px;background:#f6f6f6;border-top:1px solid var(--blue)}
.exp{position:absolute;width:276px;height:76px;display:flex;gap:8px;padding:4px 6px}
.exp.hover{background:var(--pale-yellow)}
.exp .pic{width:88px;height:68px;background:var(--sky);flex:none}
.exp h4{font-weight:normal;color:var(--blue);font-size:12px;line-height:14px;letter-spacing:.6px}
.exp p{font-size:12px;line-height:14px;letter-spacing:.6px;margin-top:3px}
.exp .site{margin-top:5px}

/* footer */
.footer{left:10px;top:1312px;width:988px;height:56px;background:var(--footer);color:#ddd;font-size:11px;letter-spacing:.6px}
</style>
</head>
<body>
<div class="page">

  <header>
    <div class="abs topbar"></div>
    <div class="abs brand"><span class="brand-mark"></span>DAYWELLSPENT.COM</div>
    <nav class="abs nav">
      <a class="current" href="#">Home</a>
      <a href="#">Find Great Times<span class="caret">▼</span></a>
      <a href="#">Promote Great Times</a>
      <a href="#">Share Great Times</a>
    </nav>
    <div class="abs account"><a href="#">Login</a> | <a href="#">Register</a></div>
    <div class="abs subband"></div>
    <div class="abs tagline">Have you lived today?</div>
    <div class="abs search-field"></div>
    <div class="abs search-btn">Search</div>
    <ul class="abs dropdown">
      <li class="active">beach gig</li>
      <li>Antarctic expedition</li>
      <li>Cambodian jungle trek</li>
      <li>Cooking and surfingclasses</li>
      <li>Sumo speed dating</li>
      <li>Drag racing and quad biking</li>
      <li>Birthday parties</li>
      <li>pub crawls and comedy nights</li>
    </ul>
  </header>

  <section class="featured">
    <div class="abs feature"></div>
    <div class="abs photo" style="left:30px;top:147px;width:390px;height:277px" role="img" aria-label="Friends preparing food together in a kitchen"></div>
    <div class="abs thumb" style="left:434px;top:145px"></div>
    <div class="abs thumb" style="left:496px;top:145px"></div>
    <div class="abs thumb" style="left:557px;top:145px"></div>
    <div class="abs thumb" style="left:620px;top:145px"></div>
    <div class="abs thumb" style="left:682px;top:145px"></div>
    <div class="abs thumb" style="left:745px;top:145px"></div>
    <div class="abs story-card">
      <h3>Title here</h3>
      <p>&nbsp;&nbsp;&nbsp;&nbsp;&nbsp;&nbsp;&nbsp;&nbsp;&nbsp;&nbsp;&nbsp;&nbsp;&nbsp;&nbsp;Description here description here description here description here description here description here description here description here description here description here description here description here description here description heredescription here description here description here description here....</p>
    </div>
    <div class="abs btn-more" style="left:856px;top:356px;width:101px">Read more</div>
    <div class="abs meta" style="left:436px;top:401px">Date here</div>
    <div class="abs meta" style="left:717px;top:401px">Posted name here</div>
    <div class="abs share"><span></span><span></span><span></span></div>
  </section>

  <section class="carousel">
    <div class="abs arrow" style="left:14px">&lt;</div>
    <div class="abs arrow" style="left:954px">&gt;</div>
    <div class="abs strip"></div>
    <div class="abs strip-thumb" style="left:96px"></div>
    <div class="abs strip-thumb" style="left:179px"></div>
    <div class="abs strip-focus"></div>
    <div class="abs photo" style="left:280px;top:452px;width:128px;height:103px;border:2px solid #ccc" role="img" aria-label="Cooking class thumbnail"></div>
    <div class="abs strip-thumb" style="left:427px"></div>
    <div class="abs strip-thumb" style="left:511px"></div>
    <div class="abs strip-thumb" style="left:594px"></div>
    <div class="abs strip-thumb" style="left:679px"></div>
    <div class="abs strip-thumb" style="left:762px"></div>
    <div class="abs strip-thumb" style="left:848px"></div>
  </section>

  <section class="latest">
    <div class="abs list-head"><span class="qmark">?</span>Title here title here tilte here</div>
    <div class="abs list-body">
      <div class="item" style="top:8px"><span class="qmark">?</span><div><h4>Title</h4><p>Description here description here and here description here and description here</p><div class="by"><span>MemberName</span><span>Date</span></div></div></div>
      <div class="item" style="top:85px"><span class="qmark">?</span><div><h4>Title</h4><p>Description here description here and here description here and description here</p><div class="by"><span>MemberName</span><span>Date</span></div></div></div>
      <div class="item hover" style="top:153px;padding-top:17px"><span class="qmark">?</span><div><h4>Title</h4><p>Description here description here and here description here and description here</p><div class="by"><span>MemberName</span><span>Date</span></div></div></div>
      <div class="item" style="top:238px"><span class="qmark">?</span><div><h4>Title</h4><p>Description here description here and here description here and description here</p><div class="by"><span>MemberName</span><span>Date</span></div></div></div>
      <div class="item" style="top:316px"><span class="qmark">?</span><div><h4>Title</h4><p>Description here description here and here description here and description here</p><div class="by"><span>MemberName</span><span>Date</span></div></div></div>
      <div class="item" style="top:392px"><span class="qmark">?</span><div><h4>Title</h4><p>Description here description here and here description here and description here</p><div class="by"><span>MemberName</span><span>Date</span></div></div></div>
      <div class="item" style="top:463px"><span class="qmark">?</span><div><h4>Title</h4><p>Description here description here and here description here and description here</p><div class="by"><span>MemberName</span><span>Date</span></div></div></div>
      <div class="item" style="top:536px"><span class="qmark">?</span><div><h4>Title</h4><p>Description here description here and here description here and description here</p><div class="by"><span>MemberName</span><span>Date</span></div></div></div>
    </div>
    <div class="abs rule-blue" style="left:38px;top:1251px;width:304px"></div>
    <div class="abs pager" style="left:110px;top:1263px">1 2 3 4 5 6 7 8 9 10....100 &nbsp;&nbsp;&nbsp;Next</div>
  </section>

  <section class="story">
    <div class="abs right"></div>
    <div class="abs read-panel">
      <div class="abs photo" style="left:14px;top:15px;width:196px;height:161px;background:linear-gradient(150deg,#5d7a3c,#2f4a22 55%,#8a7b5a)" role="img" aria-label="Travellers on a jungle trek"></div>
      <h3>Title here</h3>
      <div class="body">
        <p>The Story here the story here the story here story here the story here the story herethe story here the story here the story here the story here the story here the story here the story here the story here the srory here the story here the story here the story here the story here the story here the story here the story here the story here the story here the story here the story here the story here the story here the story</p>
        <p>he Story here the story here the story here story here the story here the story herethe story here the story here the story here the story here the story here the story here the story here the story here the srory here the story here the story here the story here the story here the story here</p>
      </div>
    </div>
    <div class="abs btn-more" style="left:859px;top:888px;width:100px;font-size:14px">Read more</div>
    <div class="abs tab" style="left:374px">Related Experiences</div>
    <div class="abs tab" style="left:584px">New Experiences</div>
    <div class="abs grid-panel">
      <div class="exp hover" style="left:16px;top:14px"><div class="pic"></div><div><h4>Title</h4><p>Some Description of the promoted place here</p><p class="site">Website here</p></div></div>
      <div class="exp" style="left:307px;top:15px"><div class="pic"></div><div><h4>Title</h4><p>Some Description of the promoted place here</p><p class="site">Website here</p></div></div>
      <div class="exp" style="left:16px;top:97px"><div class="pic"></div><div><h4>Title</h4><p>Some Description of the promoted place here</p><p class="site">Website here</p></div></div>
      <div class="exp" style="left:307px;top:97px"><div class="pic"></div><div><h4>Title</h4><p>Some Description of the promoted place here</p><p class="site">Website here</p></div></div>
      <div class="exp" style="left:16px;top:181px"><div class="pic"></div><div><h4>Title</h4><p>Some Description of the promoted place here</p><p class="site">Website here</p></div></div>
      <div class="exp" style="left:307px;top:181px"><div class="pic"></div><div><h4>Title</h4><p>Some Description of the promoted place here</p><p class="site">Website here</p></div></div>
      <div class="abs" style="left:22px;top:270px;width:565px;height:3px;background:var(--navy)"></div>
      <div class="abs pager" style="left:421px;top:283px;color:var(--navy)">1 2 3 4 5 &nbsp;&nbsp;&nbsp;&nbsp;<span style="color:var(--blue)">Next&gt; | Last</span></div>
    </div>
  </section>

  <footer class="abs footer">
    <div class="abs" style="left:23px;top:14px">Terms &amp; Condition</div>
    <div class="abs" style="left:23px;top:36px">Copyright DAYWELLSPENT.Com 2011</div>
    <div class="abs" style="left:450px;top:14px">Home | Find Great Times | Promote Great Times| Share Great Times | Login | Register</div>
  </footer>

</div>
</body>
</html>
```